Cosmetic Label Design for a Sunless Tanner

We need a label for a new sunless tanner. The label dye will be 2.5 inches in height by 6 inches in width. It will be laser printed by Brintova.net The label will be printed on gloss laminated white polypropylene self-adhesive material. A full project description can be found in the attached Word file. The label copy is also included in a Word file.

Target Market(s)

Females aged 18 to 35

Font styles to use
Serif

Colors

Designer to choose colors to be used in the design.

Requirements
Must have
• Clean look. Strong brand image.
Nice to have
• This is the first product in a future line. The design should have the ability to move to other products.
Should not have
• Too heavy. More than 4 colors. Fonts that are whimsical. Cursive writing. No cartoon like illustrations.

```html
<!DOCTYPE html>
<html lang="en">
<head>
<meta charset="utf-8">
<title>Bronzelle Skin Nourishing Sunless Tanner – Label</title>
<link rel="stylesheet" href="https://fonts.googleapis.com/css2?family=Lato:wght@300;400;700&display=swap">
<style>
  :root {
    --page-bg: #f3f3f3;
    --label-tan: #a57753;
    --label-tan-deep: #8d5e3b;
    --label-tan-light: #ad7f5a;
    --ink-dark: #1f1510;
    --ink-light: #f4e6d8;
    --warning-bg: #0d0b0a;
    --warning-ink: #ffffff;
  }
  * { box-sizing: border-box; margin: 0; padding: 0; }
  html, body { width: 1200px; height: 713px; overflow: hidden; }
  body {
    background: var(--page-bg);
    font-family: "Lato", Arial, sans-serif;
    display: flex; align-items: center; justify-content: center;
  }
  .label {
    width: 1140px; height: 475px;
    display: grid; grid-template-columns: repeat(3, 1fr);
    background: var(--label-tan);
    box-shadow: 0 2px 10px rgba(0,0,0,0.12);
  }
  .panel { position: relative; height: 100%; color: var(--ink-dark); font-size: 9.6px; line-height: 1.22; }
  .section-title { font-size: inherit; font-weight: 700; margin-bottom: 2px; }

  /* Directions panel */
  .panel--directions { padding: 42px 44px 0 38px; }
  .intro { margin-bottom: 16px; }
  .steps { list-style: none; margin-bottom: 16px; }
  .steps li { position: relative; padding-left: 14px; }
  .steps li::before { content: "•"; position: absolute; left: 2px; }
  .warning {
    position: absolute; left: 36px; bottom: 20px; width: 286px;
    background: var(--warning-bg); color: var(--warning-ink);
    padding: 7px 14px 8px 20px; font-size: 9.2px;
  }
  .warning strong { font-weight: 700; }

  /* Brand panel */
  .panel--brand {
    background: linear-gradient(180deg, var(--label-tan-light) 0%, var(--label-tan) 45%, var(--label-tan-deep) 100%);
    display: flex; flex-direction: column; align-items: center; color: var(--ink-light);
  }
  .brand-name {
    margin-top: 150px; font-weight: 400; font-size: 54px; line-height: 1;
    text-align: center; color: var(--ink-light);
  }
  .product-name {
    margin-top: 36px; font-weight: 400; font-size: 25px; line-height: 1.22;
    text-align: center; color: var(--ink-light);
  }
  .volume { position: absolute; bottom: 46px; width: 100%; text-align: center; font-size: 10.5px; color: #fff; }

  /* Ingredients panel */
  .panel--ingredients { padding: 42px 40px 0 82px; font-size: 9.2px; }
  .panel--ingredients p { margin-bottom: 9px; }
  .spacer { height: 10px; }
  .maker { position: absolute; left: 82px; top: 344px; }
  .maker strong { font-weight: 700; }
</style>
</head>
<body>
  <main class="label" aria-label="Bronzelle sunless tanner label, flat">
    <section class="panel panel--directions">
      <p class="intro">Need a tan fast? Scared of harmful effects from the sun? We've got your back! Made from the highest quality natural ingredients, Bronzelle Skin Nourishing Sunless Tanner creates a medium golden tan while providing silky-soft, color enhancing moisture to your skin.</p>
      <h2 class="section-title">Directions for use:</h2>
      <ul class="steps">
        <li>Cleanse and exfoliate skin</li>
        <li>Apply your favorite moisturizer to dryer areas like knees, elbows, ankles, and wrists</li>
        <li>Smooth a generous amount of product anywhere you'd like to tan</li>
        <li>Massage into skin</li>
        <li>Kick back and relax a minute, allowing product to dry</li>
        <li>Wash hands thoroughly with soap and water after application</li>
        <li>Watch your skin begin to glow as your tan develops over the next several hours</li>
      </ul>
      <h2 class="section-title">For best results:</h2>
      <ul class="steps">
        <li>Allow the tanner to stay on your skin for several hours before showering or swimming</li>
        <li>For an even darker look, repeat the application process for two or more days in a row</li>
        <li>Reapply as needed to achieve the results you desire</li>
      </ul>
      <p class="warning"><strong>Warning:</strong> For external use only. Does not contain sunscreen and does not protect against sunburn.</p>
    </section>

    <section class="panel panel--brand">
      <h1 class="brand-name">Bronzelle</h1>
      <p class="product-name">Skin Nourishing<br>Sunless Tanner</p>
      <p class="volume">8 fl oz (237ml)</p>
    </section>

    <section class="panel panel--ingredients">
      <h2 class="section-title">INGREDIENTS:</h2>
      <p>Water, Aloe Barbadensis Gel, Glycine Soja (Soybean) Oil, Dihydroxyacetone, Caramel, Caprylic/Capric Triglyceride, Citrus Reticulata (Mandarin Orange) Oil, Argania Spinosa (Argan) Oil, Retinyl Palmitate &amp; Ascorbyl Palmitate &amp; Tocopheryl Acetate, Saccharomyces Magnesium Ferment, Hydrolysate</p>
      <p>Saccharomyces Potassium Ferment Hydrolysate, Adenosine Triphosphate, Palmitoyl Oligopeptide &amp; Palmitoyl Tetrapeptide-7 &amp; Glycerin &amp; Butylene Glycol &amp; Carbomer &amp; Polysorbate 20, Olea Europaea (Olive) Oil, Triticum Aestivum (Wheat) Peptide, Avena Sativa (Oat) Oil, Glycine Soja (Soy) Peptide, Yeast Extract, Cupric Sulfate, Zinc Sulfate, Bana Fruit Extract, Juglans Regia (Walnut) Extract, Hydrolized Collagen, Tyrosine, Panthenol, Polyacrylamide &amp; C13-14 Isoparaffin &amp; Laureth-7, Phenoxyethanol</p>
      <div class="spacer"></div>
      <p>Dimethicone, D&amp;C Red 33 (CI 17200)</p>
      <p class="maker"><strong>www.bronzelleglow.com</strong><br>Never tested on animals<br>Manufactured for Bronzelle Skin Co. L.L.C in the USA<br>Bronzelleglow.com<br>Oakmere, NC 27000</p>
    </section>
  </main>
</body>
</html>
```